Zoravi Cantina Menu

We are looking to take a menu from excel for our new Mexican Restaurant and turn into into a classy menu that can be printed or used with a QR code link. We are located in Hawaii. We would like an easy-to-read and not over-the-top Mexican style. Elevated Mexican | Fresh Mexican We need to be able to make edits for price changes. Logo and excel spreadsheet attached.
Any colors to match our logo and mood board. Please no stock gifs and cactus...

Food on 1 page and drinks on separate pages.

```html
<!DOCTYPE html>
<html lang="en">
<head>
<meta charset="utf-8">
<title>Zoravi Cantina – Food Menu</title>
<link href="https://fonts.googleapis.com/css2?family=Della+Respira&family=Mulish:wght@400;500&family=Montserrat:wght@400;500&family=Libre+Baskerville:wght@700&display=swap" rel="stylesheet">
<style>
  :root {
    --navy: #12355b;
    --cream: #faf4ea;
    --rust: #9b4a22;
    --sky: #4a93c3;
    --ink: #3a3a3a;
    --rule: #555;
  }
  * { margin: 0; padding: 0; box-sizing: border-box; }
  html, body { width: 801px; height: 1200px; overflow: hidden; background: #fff; }
  .menu {
    position: relative; width: 801px; height: 1200px;
    background: var(--cream); overflow: hidden;
    font-family: "Mulish", sans-serif; color: var(--ink);
  }
  .masthead {
    position: absolute; left: 0; top: 0; width: 100%; height: 101px;
    background: var(--navy); color: #fff;
  }
  .brand-mark {
    position: absolute; left: 31px; top: 17px; width: 80px; height: 74px;
    border-radius: 50%; background: var(--sky);
  }
  .brand-name {
    position: absolute; left: 128px; top: 26px;
    font-family: "Montserrat", sans-serif; font-weight: 400;
    font-size: 20px; line-height: 26px; letter-spacing: 11px; color: #fff;
  }
  .masthead-rule {
    position: absolute; left: 338px; top: 24px; width: 2px; height: 60px; background: var(--sky);
  }
  .tagline {
    position: absolute; left: 363px; top: 44px;
    font-family: "Montserrat", sans-serif; font-weight: 500;
    font-size: 11.5px; letter-spacing: 5.4px; color: #fff;
  }
  .menu-title {
    position: absolute; right: 37px; top: 22px; padding-right: 8px;
    border-right: 3px solid #fff;
    font-family: "Libre Baskerville", serif; font-weight: 700;
    font-size: 27px; line-height: 30px; color: #fff; text-align: right;
  }
  .pattern-band {
    position: absolute; left: 0; width: 100%; height: 16px; background: var(--navy);
  }
  .pattern-band.top { top: 101px; }
  .pattern-band.bottom { bottom: 0; }
  .column-rule {
    position: absolute; left: 387px; top: 152px; width: 1px; height: 1006px; background: var(--rule);
  }
  .section-head {
    position: absolute; text-align: center; width: 360px;
  }
  .section-head h2 {
    font-family: "Della Respira", serif; font-weight: 400;
    font-size: 29px; line-height: 32px; color: var(--sky); letter-spacing: 0.5px;
  }
  .section-head p {
    font-size: 12.5px; line-height: 15px; color: var(--sky); letter-spacing: 0.3px;
  }
  .dish { position: absolute; }
  .dish.left { left: 33px; width: 334px; }
  .dish.right { left: 406px; width: 350px; }
  .dish h3 {
    display: flex; align-items: baseline; white-space: nowrap; overflow: hidden;
    font-family: "Della Respira", serif; font-weight: 400;
    font-size: 18.5px; line-height: 22px; color: var(--rust); letter-spacing: 0.6px;
  }
  .dish h3 .leader {
    flex: 1; overflow: hidden; min-width: 6px;
  }
  .dish h3 .leader::before {
    content: "........................................................................";
  }
  .dish p {
    font-size: 10.3px; line-height: 14.3px; color: var(--ink);
  }
</style>
</head>
<body>
<main class="menu">
  <header class="masthead">
    <div class="brand-mark"></div>
    <div class="brand-name">ZORAVI<br>&nbsp;CANTINA</div>
    <div class="masthead-rule"></div>
    <div class="tagline">FRESH MEXICAN</div>
    <div class="menu-title">FOOD<br>MENU</div>
  </header>
  <div class="pattern-band top" role="img" aria-label="Decorative zigzag and dot border"></div>

  <div class="column-rule"></div>

  <!-- Left column -->
  <div class="section-head" style="left:12px; top:148px;">
    <h2>MERIENDAS</h2>
    <p>• APPETIZERS •</p>
  </div>

  <article class="dish left" style="top:206px;">
    <h3>Island Ceviche<span class="leader"></span>$0.00</h3>
    <p>Ono fish marinated in fresh lime juice<br>and tosssed with onion, cilantro and tomato</p>
  </article>

  <article class="dish left" style="top:286px;">
    <h3>Kalua Pork Nachos<span class="leader"></span>$0.00</h3>
    <p>Freshly made local tortilla chips,<br>topped with Kalua pork, black beans,<br>cheese, guacamole, sour cream and salsa</p>
  </article>

  <article class="dish left" style="top:379px;">
    <h3>Locally made Tortilla Chips<span class="leader"></span>$0.00</h3>
    <p>*** Guacamole and traditional salsa<br>*** Traditional and grilled salsa</p>
  </article>

  <article class="dish left" style="top:458px;">
    <h3>Quesadilla<span class="leader"></span>$0.00</h3>
    <p>Large flour tortilla filled with a blend of Mild<br>cheddar and Monterey Jack cheese. Served<br>with a side of our traditional salsa<br>*** Add grilled Chicken<br>*** Add Carne Asada</p>
  </article>

  <article class="dish left" style="top:580px;">
    <h3>Zoravi Taquitos<span class="leader"></span>$0.00</h3>
    <p>(3) rolled crispy tacos, filled with shredded<br>chicken and topped with lettuce, cheese,<br>guacamole and pico de gallo</p>
  </article>

  <div class="section-head" style="left:12px; top:664px;">
    <h2>SOPA Y ENSALADA</h2>
    <p>• SOUP AND SALAD •</p>
  </div>

  <article class="dish left" style="top:736px;">
    <h3>Zoravi Tortilla Soup<span class="leader"></span>$0.00</h3>
    <p>Traditional chicken tortilla soup, topped<br>with a dollop of sour cream, cilantro and tortilla strips<br>*** Cup<br>*** Bowl</p>
  </article>

  <article class="dish left" style="top:842px;">
    <h3>Fresca Salad<span class="leader"></span>$0.00</h3>
    <p>Fresh crisp greens, corn, black beans, queso fresco<br>crumbles and tortilla strips. Our creamy cilantro<br>dressing served on the side<br>*** Add Grilled chicken<br>*** Add Carne Asada</p>
  </article>

  <article class="dish left" style="top:967px;">
    <h3>Fajita Suprema Salad<span class="leader"></span>$0.00</h3>
    <p>Large flour tostada salad bowl, filled with fresh<br>crisp greens, your choice of meat and topped<br>with guacamole,sour cream and pico de gallo<br>*** Fajita grilled chicken and veggies<br>*** Fajita gsteak and veggies</p>
  </article>

  <article class="dish left" style="top:1090px;">
    <h3>Caesar's Tijuana Salad<span class="leader"></span>$0.00</h3>
    <p>fresh romaine topped with grilled chicken<br>and tortilla strips. Our creamy ceasar<br>dressing served on the side</p>
  </article>

  <!-- Right column -->
  <div class="section-head" style="left:402px; top:148px;">
    <h2>ZORAVI'S ESPECIALES</h2>
    <p>• SPECIALS •</p>
  </div>

  <article class="dish right" style="top:216px;">
    <h3>Sizzling Fajitas<span class="leader"></span>$0.00</h3>
    <p>Sizzling platter with strips of onions and bell pepper,<br>and your choice of meat. Served with warm tortillas,<br>and your choice of beans and rice<br>*** Fajita grilled Chicken and veggies<br>*** Fajita grilled Steak and veggies<br>*** Fajita grilled Shrimp and veggies<br>*** Trio includes chicken, steak, shrimp and veggies</p>
  </article>

  <article class="dish right" style="top:363px;">
    <h3>Tacos Dorado<span class="leader"></span>$0.00</h3>
    <p>Two classic hard shell tacos, served with your choice of meat,<br>topped with lettuce, cheese and tomato, Served<br>with a side of traditional salsa<br>*** Shredded Chicken<br>*** Shredded Beef</p>
  </article>

  <article class="dish right" style="top:480px;">
    <h3>Street Tacos<span class="leader"></span>$0.00</h3>
    <p>(3) California style soft tacos topped with your choice<br>of meat and white onion and cilantro. Served<br>with a side of traditional salsa<br>*** Black Bean and Potato<br>*** Grilled Chicken<br>*** Carne Asada</p>
  </article>

  <article class="dish right" style="top:613px;">
    <h3>Birria Tacos<span class="leader"></span>$0.00</h3>
    <p>(3) corn tortillas stuffed with shredded beef, cheese,<br>onion and cilantro. Served with a side of dipping broth,<br>traditional salsa and lime wedges</p>
  </article>

  <article class="dish right" style="top:701px;">
    <h3>Grilled Ono Tacos<span class="leader"></span>$0.00</h3>
    <p>two soft corn tortillas filled with grilled Ono,<br>shredded cabbage and topped with cilantro lime crema.<br>Served with a side of traditional salsa and lime wedges</p>
  </article>

  <article class="dish right" style="top:791px;">
    <h3>Aloha Combination<span class="leader"></span>$0.00</h3>
    <p>Includes a shredded beef Taco Dorado, cheese enchilada,<br>rice and refried beans. Served with a side of traditional salsa</p>
  </article>

  <article class="dish right" style="top:867px;">
    <h3>Macho Zoravi Burrito<span class="leader"></span>$0.00</h3>
    <p>Filled with carne asada, beans De La Olla, rice, onions,<br>cilantro and guacamole. Served with a side of traditional salsa.</p>
  </article>

  <article class="dish right" style="top:943px;">
    <h3>Kalua Carnitas Platter<span class="leader"></span>$0.00</h3>
    <p>Slow cooked pork, rice, Oaxaca black beans, and tortillas.<br>Served with a side of guacamole, sour cream and traditional salsa.</p>
  </article>

  <article class="dish right" style="top:1016px;">
    <h3>Surf &amp; Turf<span class="leader"></span>$0.00</h3>
    <p>Bacon wrapped shrimp and carne asada, served<br>with beans De La Olla, rice and warm tortillas.<br>Served with your choice of spicy Diablo or garlic butter sauce.</p>
  </article>

  <article class="dish right" style="top:1106px;">
    <h3>Camarones Diablo<span class="leader"></span>$0.00</h3>
    <p>Sauteed Shrimp in a Spicy Diablo sauce, beans De La Olla,<br>rice and warm tortillas. Served with a side of sour cream.</p>
  </article>

  <div class="pattern-band bottom" role="img" aria-label="Decorative zigzag and dot border"></div>
</main>
</body>
</html>
```